Do i have coronavirus, flue or cold?

Using information from PFA and government agencies we want to make a easy to read infographic helping patients see if they have coronavirus, the flu or a cold. Using a flow diagram or whatever you think will make it easy to read and digest for the average lamen.

Information is in the word document and in the chart.

We are www.calvexa.co.uk attached is our brand guidelines, we will be putting this infographic on our website and email/sms it to all of our 300,000 patients.

```html
<!DOCTYPE html>
<html lang="en">
<head>
<meta charset="utf-8">
<title>Do I have Coronavirus, the Flu, or a Cold?</title>
<link rel="stylesheet" href="https://fonts.googleapis.com/css2?family=Archivo:ital,wght@0,700;0,800;1,700&display=swap">
<style>
  :root {
    --canvas: #f9f2ec;
    --ink: #141414;
    --navy: #1b1f4b;
    --cell: #ffffff;
    --cell-muted: #e6e7e6;
    --rule: #141414;
    --figure-top: #e9d3b0;
    --figure-bottom: #c9b07a;
  }
  * { box-sizing: border-box; margin: 0; padding: 0; }
  html, body {
    width: 1200px; height: 800px; overflow: hidden;
    background: var(--canvas);
    font-family: "Archivo", Arial, sans-serif;
  }
  .poster { position: relative; width: 1200px; height: 800px; }
  .poster-title {
    position: absolute; top: 28px; left: 0; width: 1240px;
    text-align: center;
    font-weight: 800; font-size: 44px; letter-spacing: 1.5px;
    color: var(--ink);
  }
  .symptom-table {
    position: absolute; left: 16px; top: 119px;
    display: grid;
    grid-template-columns: 122px 114px 114px 100px 110px 122px 117px 128px 123px 108px;
    grid-template-rows: 230px 142px 145px 124px;
    gap: 2px; padding: 2px;
    background: var(--rule);
  }
  .cell {
    background: var(--cell);
    color: var(--navy);
    display: flex; flex-direction: column;
    align-items: center; justify-content: center;
    text-align: center;
    font-weight: 700;
  }
  .cell.muted { background: var(--cell-muted); }
  .row-label { font-size: 22px; line-height: 1.3; }
  .symptom {
    justify-content: flex-start;
    padding-top: 36px;
  }
  .symptom-figure {
    width: 82px; height: 122px;
    border-radius: 40px 40px 8px 8px;
    background: linear-gradient(180deg, var(--figure-top), var(--figure-bottom));
  }
  .symptom-name {
    margin-top: 22px;
    font-size: 16.5px; line-height: 1.3;
    min-height: 44px;
  }
  .answer { font-size: 24px; line-height: 1.2; }
  .answer-note {
    font-style: italic; font-size: 15px; margin-top: 4px;
  }
  .answer.long { font-size: 22px; }
</style>
</head>
<body>
<main class="poster">
  <h1 class="poster-title">Do I have Coronavirus, the Flu, or a Cold ?</h1>

  <section class="symptom-table" aria-label="Symptom comparison">
    <div class="cell row-label">Symptom</div>
    <div class="cell symptom"><div class="symptom-figure" role="img" aria-label="Cartoon man with a thermometer in his mouth"></div><span class="symptom-name">Fever</span></div>
    <div class="cell symptom"><div class="symptom-figure" role="img" aria-label="Cartoon man coughing"></div><span class="symptom-name">Cough</span></div>
    <div class="cell symptom"><div class="symptom-figure" role="img" aria-label="Cartoon man yawning and sleepy"></div><span class="symptom-name">Tiredness</span></div>
    <div class="cell symptom"><div class="symptom-figure" role="img" aria-label="Cartoon man holding his chest short of breath"></div><span class="symptom-name">Shortness<br>of breath</span></div>
    <div class="cell symptom"><div class="symptom-figure" role="img" aria-label="Cartoon man with aching muscles"></div><span class="symptom-name">Muscle<br>aches</span></div>
    <div class="cell symptom"><div class="symptom-figure" role="img" aria-label="Cartoon man holding his head with a headache"></div><span class="symptom-name">Headache</span></div>
    <div class="cell symptom"><div class="symptom-figure" role="img" aria-label="Cartoon man holding his sore throat"></div><span class="symptom-name">Sore throat</span></div>
    <div class="cell symptom"><div class="symptom-figure" role="img" aria-label="Cartoon man with a runny nose and tissue"></div><span class="symptom-name">Runny nose</span></div>
    <div class="cell symptom"><div class="symptom-figure" role="img" aria-label="Cartoon man sneezing into a tissue"></div><span class="symptom-name">Sneezing</span></div>

    <div class="cell row-label">Corona<br>Virus :</div>
    <div class="cell answer">Yes</div>
    <div class="cell answer">Yes<span class="answer-note">Dry cough</span></div>
    <div class="cell answer">Yes</div>
    <div class="cell answer">Yes</div>
    <div class="cell answer">Yes</div>
    <div class="cell muted answer">Some<br>times</div>
    <div class="cell muted answer">Some<br>times</div>
    <div class="cell muted answer">Rare</div>
    <div class="cell muted answer">No</div>

    <div class="cell row-label">Flu :</div>
    <div class="cell answer">Yes<span class="answer-note">High</span></div>
    <div class="cell answer">Yes</div>
    <div class="cell answer">Yes</div>
    <div class="cell answer">Yes</div>
    <div class="cell answer">Yes<span class="answer-note">Often</span></div>
    <div class="cell answer">Yes</div>
    <div class="cell muted answer">Some<br>times</div>
    <div class="cell muted answer">Some<br>times</div>
    <div class="cell muted answer">Some<br>times</div>

    <div class="cell row-label">Cold :</div>
    <div class="cell muted answer">Rare</div>
    <div class="cell muted answer long">Moderate</div>
    <div class="cell muted answer">Mild</div>
    <div class="cell muted answer">Rare</div>
    <div class="cell muted answer long">Moderate</div>
    <div class="cell muted answer">Rare</div>
    <div class="cell answer">Yes</div>
    <div class="cell answer">Yes</div>
    <div class="cell answer">Yes</div>
  </section>
</main>
</body>
</html>
```